Problem Solving Guide- PDF Template

We are looking for an editable PDF template design for our Epoxy Floor Coatings Problem Solving Guide.

Target Market(s)

This guide will be on our website and we will also email it to customers

Industry/Entity Type

Online Shopping

Colors
f78f20
ffffff
5c5c5c
000000

Requirements
Must have
• We are looking for a very modern and clean design. Each page of the guide will address a different issue. There will be 20-25 pages in total for the completed guide, however we just need a template that we can use to create each page so that they look the same. Each page must have our logo, a spot to add a photo of the issue being discussed. Then each page will have the following sections: DESCRIPTION,CAUSE,REPAIR,PREVENTION. At the bottom of each page we would like to direct people to our website for more information. I am attaching the current guide that we have. This shows the basic information that each page will have but as you can see it is old, outdated and anything but modern. As part of the design you can put the different parts of information in circles, squares, use arrows etc. to make it appealing. I am also attaching a copy of our color chart that appears on our website to give you an idea of some of the other graphic designs that we use. Our colors are Orange (please use the same orange as in our logo) grey, black and white. Our website is www.resinmarket.net. There is also a picture of "bubbles in epoxy"-this is an example of a picture we will show to address one issue.

```html
<!DOCTYPE html>
<html lang="en">
<head>
<meta charset="utf-8">
<title>Color Differential – Problem Solving Guide</title>
<link href="https://fonts.googleapis.com/css2?family=Montserrat:wght@300;400;500;600&family=Nunito+Sans:wght@400;600;700&display=swap" rel="stylesheet">
<style>
  :root{
    --orange:#e8590c;
    --orange-dark:#d9480c;
    --grey-dark:#7b7c80;
    --grey-light:#b3b5b8;
    --slate-head:#5e5f63;
    --slate-body:#808185;
    --maroon-head:#5e1a18;
    --maroon-body:#7e1f1c;
    --ink:#111111;
    --white:#ffffff;
  }
  *{margin:0;padding:0;box-sizing:border-box}
  html,body{width:849px;height:1200px;overflow:hidden;background:var(--white)}
  body{font-family:"Nunito Sans",sans-serif;color:var(--ink);position:relative}
  .page{position:relative;width:849px;height:1200px;overflow:hidden}

  .header-art{position:absolute;left:0;top:0}
  .page-title{position:absolute;left:40px;top:54px;color:var(--white);font-family:"Montserrat",sans-serif;font-size:37px;font-weight:500;letter-spacing:.2px}

  .brand{position:absolute;left:590px;top:100px;width:232px;text-align:center}
  .brand-row{display:flex;align-items:center;justify-content:center;gap:9px}
  .brand-mark{width:18px;height:18px;background:var(--orange)}
  .brand-name{font-family:"Montserrat",sans-serif;font-size:28px;font-weight:600;color:var(--slate-head);line-height:1}
  .brand-tagline{font-family:"Montserrat",sans-serif;font-size:10.5px;font-weight:600;color:var(--slate-head);margin-top:8px}

  .section-title{font-family:"Montserrat",sans-serif;font-size:24px;font-weight:300;line-height:1}
  .body-text{font-size:15px;font-weight:400;line-height:18.8px;text-align:justify}
  .body-text b{font-weight:700}
  .para{margin-bottom:17px}

  .description{position:absolute;left:55px;top:302px;width:240px}
  .description .section-title{color:var(--orange);padding-bottom:10px;border-bottom:1.5px solid var(--orange)}
  .description p{color:var(--orange);font-size:16px;font-weight:600;line-height:20px;margin-top:10px;width:250px}

  .cause{position:absolute;left:52px;top:459px;width:334px}
  .cause .section-title{padding-bottom:11px;border-bottom:1.5px solid var(--orange);width:323px;margin-bottom:14px}
  .cause .para{margin-bottom:13px}

  .panel{position:absolute;color:var(--white)}
  .panel-head{height:var(--hh);display:flex;align-items:center;padding-left:41px}
  .panel-body{padding:14px 46px 0 41px}

  .repair{left:453px;top:435px;width:396px;height:421px;background:var(--orange)}
  .repair .panel-head{--hh:59px;background:var(--orange-dark);border-bottom:1px solid rgba(255,255,255,.35)}

  .prevention{left:0;top:856px;width:453px;height:293px;background:var(--slate-body)}
  .prevention .panel-head{--hh:56px;background:var(--slate-head);padding-left:52px}
  .prevention .panel-body{padding:16px 50px 0 52px}

  .checklist{left:453px;top:856px;width:396px;height:293px;background:var(--maroon-body)}
  .checklist .panel-head{--hh:56px;background:var(--maroon-head)}
  .checklist .panel-body{padding-top:16px}

  .footer-rule{position:absolute;left:0;top:1152px;width:849px;height:2px;background:var(--orange)}
  .footer{position:absolute;left:0;top:1169px;width:849px;text-align:center;font-size:14px}
  .footer b{font-size:16px;font-weight:700}
</style>
</head>
<body>
<main class="page">
  <svg class="header-art" width="849" height="430" viewBox="0 0 849 430">
    <circle cx="200" cy="-25" r="268" fill="var(--grey-light)"/>
    <circle cx="200" cy="-25" r="226" fill="var(--white)"/>
    <circle cx="200" cy="-25" r="218" fill="var(--grey-dark)"/>
    <circle cx="416" cy="279" r="138" fill="var(--orange)"/>
    <circle cx="416" cy="279" r="119" fill="var(--white)"/>
    <defs>
      <radialGradient id="floorTone" cx="50%" cy="65%" r="60%">
        <stop offset="0" stop-color="#9a8378"/>
        <stop offset=".6" stop-color="#6e564b"/>
        <stop offset="1" stop-color="#4d3c35"/>
      </radialGradient>
    </defs>
    <circle cx="416" cy="279" r="113" fill="url(#floorTone)" role="img" aria-label="Photo of a coated floor showing uneven colour shading"/>
  </svg>

  <h1 class="page-title">Color Differential</h1>

  <div class="brand">
    <div class="brand-row">
      <span class="brand-mark"></span>
      <span class="brand-name">resinmarket</span>
    </div>
    <div class="brand-tagline">Floor coating supplies and expert advice.</div>
  </div>

  <section class="description">
    <h2 class="section-title">Description</h2>
    <p>Difference in color or shading of topcoat.</p>
  </section>

  <section class="cause">
    <h2 class="section-title">Cause</h2>
    <div class="body-text para"><b>Retouching after 15 minutes:</b><br>Color float issues arise when a pigmented epoxy has been applied and is re-touched or rolled again after sitting for 15 minutes or longer. Different shades in the color may result.</div>
    <div class="body-text para"><b>Using different batch numbers:</b><br>Coloring can vary from batch to batch. Different batches used on the same project can result in color variances.</div>
  </section>

  <section class="panel repair">
    <div class="panel-head"><h2 class="section-title">Repair</h2></div>
    <div class="panel-body">
      <p class="body-text para">Back roll the entire area always using an 18″, woven, shed-resistant, 3/8″ nap roller. Always try to go across the entire area from side-to-side.</p>
      <p class="body-text para">When possible, recoats should always be completed with the same coating batch.</p>
      <p class="body-text para">If batches are different, blend colored (base) side first before adding activator.</p>
    </div>
  </section>

  <section class="panel prevention">
    <div class="panel-head"><h2 class="section-title">Prevention</h2></div>
    <div class="panel-body">
      <p class="body-text">If material meeds to be re-touced or rolled for any reason, it needs to be done within 10 minutes of application.</p>
    </div>
  </section>

  <section class="panel checklist">
    <div class="panel-head"><h2 class="section-title">Important Check List</h2></div>
    <div class="panel-body">
      <p class="body-text"><b>Different batch numbers :</b><br>Always check to make sure that you have the same batch number on the pigmented side of the product prior to adding the activator.</p>
    </div>
  </section>

  <div class="footer-rule"></div>
  <footer class="footer">For more information, visit us on <b>www.resinmarket.net</b></footer>
</main>
</body>
</html>
```